Re-Design Korbalex.com make it more professional looking

We want to re-design this website, we are currently not happy with existing design. Some of the design examples are listed below.

https://trelvan.com/
https://www.quostel.com/
https://www.namity.com/projects/
https://www.flarnside.com/

The content on the website is final, there will be no change in the content. We just need to re-design the site. Features page on the site is very important and need to be layout very well.

Industry/Entity Type

It Professional

Number of Pages Required

4 page

Font styles to use
Sans Serif

Requirements
Must have
• Professional look and design like the examples i quoted above and a nice color theme. I do not have preferences but i like the quostel.com and trelvan.com

```html
<!DOCTYPE html>
<html lang="en">
<head>
<meta charset="utf-8">
<title>Contact us – Korbalex</title>
<link rel="stylesheet" href="https://fonts.googleapis.com/css2?family=Dosis:wght@300;400;500;600&display=swap">
<style>
:root{
  --blue:#29a3dc;
  --orange:#f7941d;
  --text:#6f6f6f;
  --dark:#3b3f4b;
  --heading:#4a4a4a;
  --gray-bg:#f6f6f6;
  --field-border:#dedede;
  --footer-text:#c9ccd3;
  --footer-head:#ffffff;
  --icon-gray:#9a9a9a;
}
*{box-sizing:border-box;margin:0;padding:0}
html,body{width:1200px;height:2177px;overflow:hidden}
body{position:relative;font-family:"Dosis",sans-serif;color:var(--text);background:#fff}
.abs{position:absolute}

/* Hero */
.hero{position:absolute;left:0;top:0;width:1200px;height:322px;
  background:linear-gradient(120deg,#6b4a33 0%,#a27a58 35%,#8a6748 60%,#4f3626 100%)}
.hero-shade{position:absolute;inset:0;background:rgba(40,25,15,.35)}
.brand{position:absolute;left:77px;top:28px;display:flex;align-items:center;gap:8px;color:#fff;font-size:30px;font-weight:600}
.brand-dot{width:26px;height:26px;border-radius:50%;background:var(--orange)}
.nav{position:absolute;top:30px;left:0;width:1200px;height:32px}
.nav a{position:absolute;top:0;height:32px;line-height:32px;color:#fff;text-decoration:none;font-size:15px;text-align:center}
.nav .active{background:var(--orange);border-radius:16px;width:88px}
.nav .login{border:1.5px solid #fff;border-radius:16px;width:88px;line-height:29px}
.hero-title{position:absolute;top:163px;width:1200px;text-align:center;color:#fff;font-size:33px;font-weight:400}
.hero-sub{position:absolute;top:207px;width:1200px;text-align:center;color:#fff;font-size:18px;font-weight:300}

/* Location */
.section-title{position:absolute;left:152px;color:var(--blue);font-size:24px;font-weight:400}
.map{position:absolute;left:152px;top:438px;width:589px;height:282px;border:4px solid #eee;
  background:linear-gradient(135deg,#ece9e2 0%,#e4e1d8 50%,#dfe6d5 100%)}
.office{position:absolute;left:767px;top:434px;width:300px;font-size:14px;line-height:20px;font-weight:300}
.office h4{font-size:14px;font-weight:500;color:var(--heading);margin-bottom:8px}
.office .label{font-weight:500;color:var(--heading);margin-top:20px;margin-bottom:4px}
.office .phone{font-size:19px;font-weight:400;color:#555}
.social{display:flex;gap:9px;margin-top:8px}
.social span{width:20px;height:20px;border-radius:3px;background:var(--icon-gray)}

/* Form */
.contact-band{position:absolute;left:0;top:785px;width:1200px;height:385px;background:var(--gray-bg)}
.field{position:absolute;height:32px;background:#fff;border:1px solid var(--field-border);font-size:13px;color:#aaa;padding:8px 10px;font-weight:300}
.send{position:absolute;left:152px;top:1073px;width:98px;height:31px;background:var(--blue);color:#fff;font-size:15px;display:flex;align-items:center;justify-content:center;gap:8px}

/* Testimonial */
.testimonial{position:absolute;left:0;top:1170px;width:1200px;height:603px;
  background:linear-gradient(180deg,#f3f3f3 0%,#ececec 50%,#f4f4f4 100%)}
.avatar{position:absolute;left:552px;top:1235px;width:96px;height:96px;border-radius:50%;background:linear-gradient(160deg,#c9cdd2,#7f868f);border:3px solid #fff}
.quote{position:absolute;left:250px;top:1352px;width:700px;text-align:center;font-size:14px;line-height:18px;font-weight:300;color:#555}
.person{position:absolute;top:1458px;width:1200px;text-align:center;font-size:15px;color:#444}
.role{position:absolute;top:1479px;width:1200px;text-align:center;font-size:13px;font-weight:300;color:#666}
.dots{position:absolute;top:1529px;left:566px;display:flex;gap:8px}
.dots i{width:5px;height:5px;border-radius:50%;background:#c4c4c4}
.dots i.on{background:var(--blue)}
.cta-line{position:absolute;left:152px;top:1610px;width:895px;height:1px;background:var(--blue)}
.cta-title{position:absolute;top:1593px;width:1200px;text-align:center;color:var(--blue);font-size:24px}
.cta-sub{position:absolute;top:1624px;width:1200px;text-align:center;color:var(--blue);font-size:14px;font-weight:300}
.cta-btn{position:absolute;left:500px;top:1669px;width:200px;height:39px;background:var(--orange);color:#fff;font-size:15px;line-height:39px;text-align:center}

/* Footer */
.footer{position:absolute;left:0;top:1773px;width:1200px;height:404px;background:var(--dark)}
.fcol{position:absolute;top:1830px;font-size:14px;line-height:25px;color:var(--footer-text);font-weight:300}
.fcol h5{font-size:15px;font-weight:500;color:var(--footer-head);margin-bottom:12px}
.fcol a{display:block;color:inherit;text-decoration:none}
.fcol a.hl{color:var(--blue);text-decoration:underline}
.fcall{font-size:19px;line-height:26px}
.fsocial{display:flex;gap:9px;margin-top:6px}
.fsocial span{width:20px;height:20px;border-radius:3px;background:#d5d7dc}
.fsocial span.on{background:var(--blue)}
.blog a{line-height:19px;margin-bottom:14px}
.divider{position:absolute;left:130px;top:2086px;width:940px;height:1px;background:#50556070}
.copy{position:absolute;left:152px;top:2124px;font-size:13px;color:var(--footer-text);font-weight:300}
.totop{position:absolute;left:1012px;top:2116px;width:34px;height:34px;border-radius:50%;background:var(--orange)}
</style>
</head>
<body>

<header class="hero" role="img" aria-label="Desk scene with glasses, a red coffee cup and a notebook">
  <div class="hero-shade"></div>
</header>
<div class="brand"><span class="brand-dot"></span>Korbalex</div>
<nav class="nav">
  <a class="active" style="left:502px">Home</a>
  <a style="left:610px;width:70px">Features</a>
  <a style="left:712px;width:70px">Pricing</a>
  <a style="left:810px;width:70px">About Us</a>
  <a style="left:917px;width:90px">Contact Us</a>
  <a class="login" style="left:1035px">Login</a>
</nav>
<h1 class="hero-title">Contact us</h1>
<p class="hero-sub">Customers are our first priority. Feel free to ask for any assistance</p>

<h2 class="section-title" style="top:382px">Where we're located</h2>
<div class="map" role="img" aria-label="Street map showing the office location"></div>
<div class="office">
  <h4>Norvale IT Services Pvt. Ltd.</h4>
  <p>Plot No 18 Meridian Vatika Ext<br>Lakeview Road, Jaipur- 302011<br>(Rajasthan) India</p>
  <p class="label">Contact Info</p>
  <p class="phone">+1-555-010-2846</p>
  <p>+91-141-5550142 / +91-90000-55512<br>help@korbalex.com</p>
  <p class="label" style="margin-top:24px">Follow Us</p>
  <div class="social" aria-label="Social links"><span></span><span></span><span></span><span></span></div>
</div>

<section class="contact-band"></section>
<h2 class="section-title" style="top:843px">We'd love to hear from you</h2>
<div class="field" style="left:152px;top:897px;width:282px">Name</div>
<div class="field" style="left:459px;top:897px;width:282px">Email</div>
<div class="field" style="left:765px;top:897px;width:282px">Phone</div>
<div class="field" style="left:152px;top:952px;width:895px;height:96px">Type your Message ...</div>
<div class="send">
  <svg width="15" height="13" viewBox="0 0 15 13"><path d="M0 6 L15 0 L11 13 L7 8 Z" fill="#fff"/></svg>Send
</div>

<section class="testimonial" role="img" aria-label="Faded desk scene background"></section>
<div class="avatar" role="img" aria-label="Portrait of the reviewer"></div>
<svg class="abs" style="left:170px;top:1342px" width="22" height="38" viewBox="0 0 22 38"><path d="M20 2 L3 19 L20 36" fill="none" stroke="#777" stroke-width="2"/></svg>
<svg class="abs" style="left:1010px;top:1342px" width="22" height="38" viewBox="0 0 22 38"><path d="M2 2 L19 19 L2 36" fill="none" stroke="#777" stroke-width="2"/></svg>
<p class="quote">We tested different project management tools, but none of them came close to the simplicity and power of Korbalex's SEO Management Tool. It was surprising to see how so many companies missed the beat? Well, I don't have the answer of it, but one thing is for sure Korbalex SEO project management tool is exactly what we needed that too at a price to match.</p>
<p class="person">Marcus Hale</p>
<p class="role">Project Manager at Brightwell Ops</p>
<div class="dots"><i></i><i></i><i></i><i></i><i></i><i class="on"></i><i></i></div>
<div class="cta-line"></div>
<h2 class="cta-title">Get started on Korbalex</h2>
<p class="cta-sub">Share your experience with us and get 3 months of premium access for free</p>
<div class="cta-btn">Start My 30 Day Free Trial</div>

<footer class="footer"></footer>
<div class="fcol" style="left:152px">
  <h5>Quick Link</h5>
  <a>Home</a><a class="hl">About Us</a><a>Features</a><a>Pricing</a><a>Contact Us</a><a>Sitemap</a>
</div>
<div class="fcol" style="left:307px">
  <h5>Resources</h5>
  <a>Testimonials</a><a>3rd Party Apps</a><a>Newsletters</a><a>Support &amp; FAQs</a><a>Privacy Policy</a><a>Refund Policy</a>
</div>
<div class="fcol" style="left:457px">
  <h5>Help &amp; Support</h5>
  <p class="fcall">Call Us: +1-555-010-2846</p>
  <p>help@korbalex.com</p>
  <h5 style="margin-top:22px;margin-bottom:4px">Follow Us</h5>
  <div class="fsocial"><span></span><span class="on"></span><span></span><span></span></div>
</div>
<div class="fcol blog" style="left:765px;width:290px">
  <h5>Latest in Korbalex Blog</h5>
  <a>Combating Fear, the Productivity Killer (Work Management Roundup)</a>
  <a class="hl">10 Suggestions to Improve Your Marketing Operations from Leaders</a>
  <a>How to Create an Incredible Onboarding Experience For Your New Hires</a>
  <a style="text-decoration:underline">» View All Blog</a>
</div>
<div class="divider"></div>
<p class="copy">© 2016, Korbalex by Norvale service Pvt. Ltd. All Rights Reserved.</p>
<div class="totop">
  <svg width="34" height="34" viewBox="0 0 34 34"><path d="M11 19 L17 13 L23 19" fill="none" stroke="#fff" stroke-width="2.5"/></svg>
</div>

</body>
</html>
```